Business Card Design using new logo

As much as we'd like to think that treating everyone equally is the best strategy for fairness, the reality is that the differences in the lives of women and men have to be taken into account to ensure that organizations, programs, services, and yes, even public policy treat women and men in ways that achieve gender equity.

That's where ParityLumen - fairness metrics insight comes in. Using the data-driven tools of gender analysis, our organization can help anyone determine if gender equity is being achieved - in businesses and organizations, in the planning and implementation of programs and services, and in the development and enforcement of public policy.
Updates

Apologies for the delay - have not had time to finalize the decision.  Should be early this week - probably Tuesday.

Industry/Entity Type

Business

Requirements
Must have
• New Logo for ParityLumen
• Logo plus words "Fairness Metrics Insight"

```html
<!DOCTYPE html>
<html lang="en">
<head>
<meta charset="utf-8">
<title>ParityLumen – Business Cards</title>
<link href="https://fonts.googleapis.com/css2?family=Open+Sans:wght@400;600&display=swap" rel="stylesheet">
<style>
  :root {
    --backdrop: #d9d9d9;
    --card-dark: #414141;
    --card-light: #f4f4f4;
    --accent: #ef9a2a;
    --ink-dark: #3a3a3a;
    --ink-light: #ffffff;
    --divider: #9a9a9a;
  }
  * { margin: 0; padding: 0; box-sizing: border-box; }
  html, body {
    width: 1200px; height: 900px; overflow: hidden;
    background: var(--backdrop);
    font-family: "Open Sans", Arial, sans-serif;
  }
  .sheet {
    width: 1200px; height: 900px;
    display: flex; align-items: center; justify-content: center; gap: 40px;
  }
  .card {
    width: 540px; height: 300px;
    box-shadow: 0 10px 24px rgba(0,0,0,0.18);
    position: relative; overflow: hidden;
  }

  /* Front */
  .card-front {
    background: var(--card-dark);
    display: flex; align-items: center; justify-content: center;
  }
  .front-lockup { display: flex; align-items: center; gap: 14px; }
  .brand-dot {
    width: 44px; height: 44px; border-radius: 50%;
    background: var(--accent); flex: none;
  }
  .front-text { display: flex; flex-direction: column; }
  .front-name {
    color: var(--ink-light); font-weight: 600; font-size: 38px; line-height: 1.05;
  }
  .front-tagline {
    color: var(--accent); font-size: 17px; font-weight: 400; margin-top: 2px;
  }
  .front-web {
    color: var(--ink-light); font-size: 12px; letter-spacing: 1px;
    margin-top: 4px; align-self: flex-end;
  }

  /* Back */
  .card-back { display: flex; }
  .back-brand {
    width: 52%; background: var(--card-light);
    display: flex; align-items: center; justify-content: center; gap: 10px;
  }
  .back-brand .brand-dot { width: 30px; height: 30px; }
  .back-name {
    color: var(--ink-dark); font-weight: 600; font-size: 27px;
  }
  .back-details {
    width: 48%; background: var(--card-dark);
    padding: 48px 28px 0 30px; position: relative;
  }
  .back-details::before {
    content: ""; position: absolute; left: 0; top: 52px;
    width: 3px; height: 90px; background: var(--divider);
  }
  .person-name {
    color: var(--ink-light); font-weight: 600; font-size: 17px;
    letter-spacing: 0.3px; margin-bottom: 26px;
  }
  .contact-list { list-style: none; }
  .contact-item {
    display: flex; align-items: center; gap: 12px;
    color: var(--ink-light); font-size: 12px; line-height: 1; margin-bottom: 9px;
    letter-spacing: 0.3px;
  }
  .contact-icon { width: 10px; height: 10px; flex: none; fill: var(--accent); }
</style>
</head>
<body>
<main class="sheet">
  <section class="card card-front" aria-label="Business card front">
    <div class="front-lockup">
      <span class="brand-dot"></span>
      <div class="front-text">
        <span class="front-name">ParityLumen</span>
        <span class="front-tagline">Fairness Metrics Insight</span>
        <span class="front-web">www.paritylumen.com</span>
      </div>
    </div>
  </section>

  <section class="card card-back" aria-label="Business card back">
    <div class="back-brand">
      <span class="brand-dot"></span>
      <span class="back-name">ParityLumen</span>
    </div>
    <div class="back-details">
      <p class="person-name">Maren Holloway</p>
      <ul class="contact-list">
        <li class="contact-item">
          <svg class="contact-icon" viewBox="0 0 10 10" aria-hidden="true"><path d="M2 0.5 L3.6 2.6 L2.7 3.6 Q3.6 5.8 6.4 7.3 L7.4 6.4 L9.5 8 L8.2 9.5 Q3.8 9 0.5 1.8 Z"/></svg>
          353 555 0140
        </li>
        <li class="contact-item">
          <svg class="contact-icon" viewBox="0 0 10 10" aria-hidden="true"><rect x="1.5" y="0.5" width="7" height="9" rx="1"/><rect x="3" y="2" width="4" height="2" fill="#414141"/></svg>
          353 555 0141
        </li>
        <li class="contact-item">
          <svg class="contact-icon" viewBox="0 0 10 10" aria-hidden="true"><rect x="0.5" y="2" width="9" height="6.5"/><path d="M0.5 2 L5 5.6 L9.5 2" fill="none" stroke="#414141" stroke-width="1"/></svg>
          info@paritylumen.com
        </li>
        <li class="contact-item">
          <svg class="contact-icon" viewBox="0 0 10 10" aria-hidden="true"><circle cx="5" cy="5" r="4.5"/></svg>
          @Parity_Lumen
        </li>
      </ul>
    </div>
  </section>
</main>
</body>
</html>
```